Brand new letterhead, business card, email signature etc.

We are a financial company in London, UK. Our website is www.quorvane.com. We're wanting a complete remodel of the company colours, letter head, business cards, email signatures, etc. Looking to keep the same font for the company name. I have upload a colour palette that we want to work with. We're looking for company letterhead for outgoing letters/ correspondence, letterhead for internal documentation, email signatures, e-letters. etc. Ultimately we will redesign the entire website also. It is important that our clients get a strong, secure, warm, trustworthy, solid feeling and first impression.
Updates

Designs look the same

Target Market(s)

Institutional investors, (ultra) high net worth individuals

Industry/Entity Type

Finance, Invesments banking.

Font styles to use
Other font styles liked:
• Current font is "Champagne & Limousines"

Requirements
Must have
• Must use the colours provided on the PDF uploaded to the portal. The purple = main colour. The red = accent colour.
Nice to have
• Nice to use same font as now for the company name "Marlowin". Font is "Champagne & Limousines". Nice to have some reference to the old logo flower, but only subtle.
Should not have
• Do not use the colour red from our website. Use the colours provided on the colour palette PDF that I uploaded in the portal.

```html
<!DOCTYPE html>
<html lang="en">
<head>
<meta charset="utf-8">
<title>Marlowin Stationery Set</title>
<link rel="stylesheet" href="https://fonts.googleapis.com/css2?family=Josefin+Sans:wght@300;400;600&display=swap">
<style>
  :root {
    --stage: #666666;
    --plum: #2d0c1c;
    --accent: #e0412f;
    --rule: #f09a86;
    --paper: #ffffff;
    --ink: #2a2a2a;
    --muted: #6d6d6d;
    --label: #f2f2f2;
    --font: "Josefin Sans", sans-serif;
  }
  * { box-sizing: border-box; margin: 0; padding: 0; }
  html, body { width: 1200px; height: 910px; overflow: hidden; }
  body { background: var(--stage); font-family: var(--font); position: relative; }

  .sheet-label {
    position: absolute; color: var(--label); font-weight: 300; font-size: 17px;
    letter-spacing: 0.5px; transform: translateX(-50%); white-space: nowrap;
  }

  .shadowed { box-shadow: 0 6px 22px rgba(0,0,0,0.35); }

  /* Wordmark */
  .wordmark { position: absolute; display: flex; align-items: center; transform: translate(-50%, -50%); white-space: nowrap; }
  .wordmark__square { border: 1px solid currentColor; flex: none; }
  .wordmark__name { font-weight: 300; text-transform: uppercase; line-height: 1; }

  /* Letterhead */
  .letterhead { position: absolute; left: 67px; top: 91px; width: 518px; height: 731px; background: var(--paper); }
  .letterhead__band { position: absolute; left: 0; top: 0; width: 100%; height: 9px; background: var(--plum); }
  .letterhead .wordmark { left: 259px; top: 51px; color: var(--ink); }
  .letterhead .wordmark__square { width: 39px; height: 39px; margin-right: 9px; }
  .letterhead .wordmark__name { font-size: 22px; letter-spacing: 5px; }
  .letterhead__rule { position: absolute; left: 28px; top: 85px; width: 463px; height: 1px; background: var(--rule); }
  .letterhead__watermark {
    position: absolute; left: 142px; top: 232px; width: 236px; height: 252px; border-radius: 50%;
    background: radial-gradient(circle, rgba(240,240,240,0.9) 0%, rgba(246,246,246,0.5) 55%, rgba(255,255,255,0) 75%);
  }
  .letterhead__footer { position: absolute; left: 0; top: 669px; width: 100%; height: 52px; }
  .footer-col {
    position: absolute; top: 0; height: 52px; text-align: center; color: var(--muted);
    font-size: 8.6px; font-weight: 300; line-height: 12px;
  }
  .footer-col svg { display: block; margin: 3px auto 6px; width: 17px; height: 17px; }
  .footer-col--contact { left: 0; width: 178px; }
  .footer-col--london { left: 178px; width: 162px; border-left: 1px solid var(--rule); }
  .footer-col--island { left: 340px; width: 178px; border-left: 1px solid var(--rule); }

  /* Business card front */
  .card { position: absolute; width: 438px; height: 250px; }
  .card--front { left: 670px; top: 91px; background: var(--paper); }
  .card--front .wordmark { left: 224px; top: 51px; color: var(--ink); }
  .card .wordmark__square { width: 54px; height: 54px; margin-right: 13px; }
  .card .wordmark__name { font-size: 27px; letter-spacing: 6px; }
  .card__line { position: absolute; left: 0; top: 122px; width: 100%; height: 2px; background: var(--plum); }
  .card__badge {
    position: absolute; left: 125px; top: 104px; width: 189px; height: 38px; border-radius: 19px;
    background: var(--plum); color: #fff; text-align: center; padding-top: 4px;
  }
  .card__name { font-size: 19px; font-weight: 400; line-height: 19px; }
  .card__role { font-size: 12.5px; font-weight: 400; line-height: 13px; }
  .contact-list { position: absolute; list-style: none; color: var(--ink); }
  .contact-list li { display: flex; align-items: flex-start; }
  .contact-list svg { flex: none; }
  .card .contact-list { top: 172px; font-size: 13.5px; line-height: 19px; }
  .card .contact-list svg { width: 12px; height: 12px; margin: 2px 7px 0 0; }
  .card .contact-list--left { left: 44px; }
  .card .contact-list--right { left: 217px; }

  /* Business card back */
  .card--back { left: 670px; top: 380px; background: var(--plum); }
  .card--back .wordmark { left: 224px; top: 125px; color: #fff; }

  /* Email signature */
  .signature { position: absolute; left: 680px; top: 675px; width: 348px; height: 146px; background: var(--paper); }
  .signature__photo {
    position: absolute; left: 38px; top: 25px; width: 62px; height: 62px;
    background: linear-gradient(160deg, #a9d3d6 0%, #8fc2c6 50%, #3a3b44 100%);
  }
  .signature__name { position: absolute; left: 0; width: 138px; top: 94px; text-align: center; color: var(--ink); font-size: 13.5px; line-height: 14px; }
  .signature__role { position: absolute; left: 0; width: 138px; top: 108px; text-align: center; color: var(--muted); font-size: 11.5px; font-weight: 300; }
  .signature__divider { position: absolute; left: 135px; top: 11px; width: 1.5px; height: 123px; background: var(--plum); }
  .signature .contact-list { left: 149px; top: 20px; font-size: 9.6px; line-height: 13.6px; }
  .signature .contact-list li { margin-bottom: 4.8px; }
  .signature .contact-list svg { width: 8px; height: 8px; margin: 2px 4px 0 0; }
</style>
</head>
<body>
<svg width="0" height="0" style="position:absolute" aria-hidden="true">
  <defs>
    <symbol id="icon-phone" viewBox="0 0 24 24">
      <path d="M6.5 2.5l3 4-2 2.2c1.2 2.9 3.5 5.3 6.5 6.6l2.2-2 4 3-1.8 3.4c-8.5-.5-15-7.1-15.3-15.5z" fill="none" stroke="#e0412f" stroke-width="2" stroke-linejoin="round"/>
    </symbol>
    <symbol id="icon-mail" viewBox="0 0 24 24">
      <rect x="2" y="5" width="20" height="14" fill="#e0412f"/>
      <path d="M2 5l10 8 10-8M2 19l7.5-7M22 19l-7.5-7" fill="none" stroke="#fff" stroke-width="1.5"/>
    </symbol>
    <symbol id="icon-globe" viewBox="0 0 24 24">
      <g fill="none" stroke="#e0412f" stroke-width="1.8">
        <circle cx="12" cy="12" r="9.5"/><ellipse cx="12" cy="12" rx="4.2" ry="9.5"/>
        <path d="M2.5 12h19M4 7h16M4 17h16"/>
      </g>
    </symbol>
    <symbol id="icon-pin" viewBox="0 0 24 24">
      <path d="M12 2a6.5 6.5 0 0 0-6.5 6.5C5.5 13.5 12 20 12 20s6.5-6.5 6.5-11.5A6.5 6.5 0 0 0 12 2z" fill="none" stroke="#e0412f" stroke-width="2"/>
      <circle cx="12" cy="8.5" r="2.3" fill="#e0412f"/>
      <path d="M7 22h10" stroke="#e0412f" stroke-width="2"/>
    </symbol>
    <symbol id="icon-pin-solid" viewBox="0 0 24 24">
      <path d="M12 1a7 7 0 0 0-7 7c0 5.5 7 12 7 12s7-6.5 7-12a7 7 0 0 0-7-7z" fill="#e0412f"/>
      <circle cx="12" cy="8" r="2.6" fill="#fff"/>
      <path d="M6 17l-4 6h20l-4-6" fill="none" stroke="#e0412f" stroke-width="1.6" stroke-linejoin="round"/>
    </symbol>
  </defs>
</svg>

<span class="sheet-label" style="left:320px;top:50px">Leterhead</span>
<span class="sheet-label" style="left:882px;top:50px">Card Front</span>
<span class="sheet-label" style="left:882px;top:355px">Card Back</span>
<span class="sheet-label" style="left:898px;top:645px">Email Signature</span>

<section class="letterhead shadowed">
  <div class="letterhead__band"></div>
  <div class="wordmark"><span class="wordmark__square"></span><span class="wordmark__name">Marlowin</span></div>
  <div class="letterhead__rule"></div>
  <div class="letterhead__watermark" role="img" aria-label="Faint brand flower decoration"></div>
  <footer class="letterhead__footer">
    <div class="footer-col footer-col--contact">
      <svg><use href="#icon-globe"/></svg>
      info@marlowin.com | +00 1200 340056<br>www.quorvane.com
    </div>
    <div class="footer-col footer-col--london">
      <svg><use href="#icon-pin-solid"/></svg>
      Marlowin Group Limited, 11th Floor,<br>12 Fenwick Row, London, EC3B 7QT
    </div>
    <div class="footer-col footer-col--island">
      <svg><use href="#icon-pin-solid"/></svg>
      Marlowin (IOM) Limited, Harbour Court,<br>Douglas, Isle of Man, IM98 2TL
    </div>
  </footer>
</section>

<section class="card card--front shadowed">
  <div class="wordmark"><span class="wordmark__square"></span><span class="wordmark__name">Marlowin</span></div>
  <div class="card__line"></div>
  <div class="card__badge">
    <div class="card__name">DANIEL REEVE</div>
    <div class="card__role">Managing Director</div>
  </div>
  <ul class="contact-list contact-list--left">
    <li><svg><use href="#icon-phone"/></svg>+00 1200 340056</li>
    <li><svg><use href="#icon-mail"/></svg>info@marlowin.com</li>
    <li><svg><use href="#icon-globe"/></svg>www.quorvane.com</li>
  </ul>
  <ul class="contact-list contact-list--right">
    <li><svg><use href="#icon-pin"/></svg><span>Marlowin Group Limited,<br>11th Floor, 12 Fenwick Row,<br>London, EC3B 7QT</span></li>
  </ul>
</section>

<section class="card card--back shadowed">
  <div class="wordmark"><span class="wordmark__square"></span><span class="wordmark__name">Marlowin</span></div>
</section>

<section class="signature shadowed">
  <div class="signature__photo" role="img" aria-label="Portrait photo of the managing director"></div>
  <div class="signature__name">DANIEL REEVE</div>
  <div class="signature__role">Managing Director</div>
  <div class="signature__divider"></div>
  <ul class="contact-list">
    <li><svg><use href="#icon-phone"/></svg>+00 1200 340056</li>
    <li><svg><use href="#icon-mail"/></svg>info@marlowin.com</li>
    <li><svg><use href="#icon-globe"/></svg>www.quorvane.com</li>
    <li><svg><use href="#icon-pin"/></svg><span>Marlowin Group Limited, 11th Floor,<br>12 Fenwick Row, London, EC3B 7QT</span></li>
    <li><svg><use href="#icon-pin"/></svg><span>Marlowin (IOM) Limited, Harbour Court,<br>Douglas, Isle of Man, IM98 2TL</span></li>
  </ul>
</section>
</body>
</html>
```